Pelo Rang Brewery looking for beer label design

Pelo Rang Brewery is an up and coming small brewery in Bangkok, Thailand. We are looking for label designs that incorporate the Thai Tuk Tuk "motorcycle" in the label. Also it should be a label that easily can be varied to show the various kind of beers, such as e.g. IPA, Porter, Lager etc.
We are looking for a fun, humor filled design
Brewery

```html
<!DOCTYPE html>
<html lang="en">
<head>
<meta charset="utf-8">
<title>Pelo Rang Brewery – Pale Ale Label</title>
<link rel="stylesheet" href="https://fonts.googleapis.com/css2?family=Oswald:wght@700&display=swap">
<style>
  :root {
    --backdrop: #e6d2b4;
    --night-top: #141d45;
    --night-bottom: #2b3c7c;
    --moon-light: #f3ecd6;
    --moon-shade: #b8b09a;
    --ink: #1c1a22;
    --silhouette: #3a3640;
    --flame: #e0903a;
    --gold: #d9a441;
    --cream: #efe6cf;
  }
  html, body {
    margin: 0;
    padding: 0;
    width: 1200px;
    height: 1200px;
    overflow: hidden;
    background: var(--backdrop);
  }
  .canvas {
    position: relative;
    width: 1200px;
    height: 1200px;
  }
  .label {
    position: absolute;
    left: 205px;
    top: 50px;
    width: 790px;
    height: 1100px;
    display: block;
  }
  .label text {
    font-family: "Oswald", "Arial Narrow", sans-serif;
    font-weight: 700;
  }
  .brand-name { fill: var(--ink); }
  .beer-style { fill: var(--gold); letter-spacing: 4px; }
  .spec { fill: var(--cream); }
</style>
</head>
<body>
<main class="canvas">
  <svg class="label" viewBox="0 0 790 1100" xmlns="http://www.w3.org/2000/svg">
    <defs>
      <linearGradient id="night-sky" x1="0" y1="0" x2="0" y2="1">
        <stop offset="0" stop-color="var(--night-top)"/>
        <stop offset="1" stop-color="var(--night-bottom)"/>
      </linearGradient>
      <radialGradient id="moon-glow" cx="0.45" cy="0.45" r="0.6">
        <stop offset="0" stop-color="var(--moon-light)"/>
        <stop offset="1" stop-color="var(--moon-shade)"/>
      </radialGradient>
      <linearGradient id="ride-tone" x1="0" y1="0" x2="1" y2="0">
        <stop offset="0" stop-color="var(--silhouette)"/>
        <stop offset="0.75" stop-color="var(--silhouette)"/>
        <stop offset="1" stop-color="var(--flame)"/>
      </linearGradient>
      <path id="style-arc" d="M 150 880 Q 380 1010 610 880"/>
    </defs>

    <rect class="label-field" width="790" height="1100" fill="url(#night-sky)"/>

    <circle class="moon" cx="380" cy="465" r="335" fill="url(#moon-glow)"/>

    <g class="brand">
      <text class="brand-name" x="380" y="325" font-size="96" text-anchor="middle">PELO RANG</text>
      <text class="brand-name" x="610" y="398" font-size="40" text-anchor="end" letter-spacing="3">BREWERY</text>
    </g>

    <rect class="ride-illustration" x="175" y="440" width="470" height="220" rx="24"
          fill="url(#ride-tone)" opacity="0.85"
          role="img" aria-label="Tuk tuk silhouette flying across the moon on a rocket flame with a smoke trail"/>

    <text class="beer-style" font-size="84">
      <textPath href="#style-arc" startOffset="50%" text-anchor="middle">PALE ALE</textPath>
    </text>

    <text class="spec" x="50" y="1005" font-size="34">350ml</text>
    <text class="spec" x="740" y="1005" font-size="34" text-anchor="end">6% ALC.</text>

    <rect class="gold-rule" x="0" y="1044" width="790" height="10" fill="var(--gold)"/>
    <rect class="gold-rule" x="0" y="1068" width="790" height="4" fill="var(--gold)"/>
  </svg>
</main>
</body>
</html>
```